Create design for Dark Theme Website

We are a solar company wanting a website that has clean crisp feel of Pearfield. We like the dark contrasting theme in the Vorlan Cellbank and Brightmoor House Charge websites listed below. We want a dark theme with single scroll down style page.
See the following for theme and look:
https://www.vorlan-example.com/sunarrays
https://brightmoorhousecharge-example.com/

Our current website for further information is http://quillstonesun-example.co.nz

We want the following sections on the single page as they scroll down:
1. Main Landing page for Quill Stone Solar.
2. About us - company / service description
3. How it works - animation showing house with powerlines. The animations will show 'on-grid' day time, on-grid night time, Hybrid day time, Hybrid nightime / or stormy weather)
4. Mobile / monitoring - We like the brightmoor photo style. We want to show our app on phone.
5. Home installation location - SHow location of installation and details about requirements
6. Solution Specifications Section- A button product filter, basic specs are shown on site (like vorlan buy now) - really detailed information on brochure (like brightmoor size selection)
7. Request Solutions Consultant form - if you want a quote, done in form style (Name, email, phone)
8. Estimator - (price estimator like vorlan buy now) would have address finder, home bedroom count, install timeframe, contact details (first name, last name, email, phone, contact time preference)

I have uploaded our two brochures and some example diagrams for reference and image material.

Target Market(s)

Solar Energy Customers, wanting ongrid, off-grid or hybrid microgrids or solar energy solutions.

Industry/Entity Type

Solar Energy

Coding

Number of Pages Required

Font styles to use
Sans Serif

Requirements
Must have
• The dark theme to match the company name and themes used by Vorlan and Brightmoor. Want a single scroll down page
Nice to have
• Nice transitions and animations to show different types of microgrid.

```html
<!DOCTYPE html>
<html lang="en">
<head>
<meta charset="utf-8">
<title>Quill Stone Solar — Off-Grid Lithium Solar Energy Solutions</title>
<link href="https://fonts.googleapis.com/css2?family=Poppins:wght@300;400;500;600&display=swap" rel="stylesheet">
<style>
:root{
  --bg:#151515;
  --bg-panel:#1c1c1c;
  --bg-deep:#111111;
  --field:#2a2a2a;
  --green:#8cc63f;
  --white:#ffffff;
  --text:#d8d8d8;
  --muted:#9a9a9a;
}
*{margin:0;padding:0;box-sizing:border-box}
html,body{width:1200px;height:5051px;overflow:hidden;background:var(--bg);font-family:'Poppins',sans-serif;color:var(--text)}
.section{position:relative;width:1200px;overflow:hidden}
.abs{position:absolute}
.wordmark{font-family:'Poppins',sans-serif;font-weight:500;color:var(--white);letter-spacing:1px}
/* hero */
.hero{height:631px;background:linear-gradient(135deg,#1d1d1d 0%,#0e0e0e 45%,#1a1a1a 70%,#0c0c0c 100%)}
.hero .wordmark{left:46px;top:34px;font-size:22px}
.nav{right:46px;top:42px;display:flex;gap:30px;font-size:12.5px;color:var(--white)}
.nav .active{color:var(--green)}
.hero-title{left:0;width:1200px;top:272px;text-align:center;font-size:27px;font-weight:600;color:var(--white);line-height:36px}
.feature{top:492px;width:260px;text-align:center;font-size:13.5px;color:var(--white)}
.feature svg{display:block;margin:0 auto 14px}
/* split sections */
.split{height:632px}
.photo{top:0;height:100%}
.eyebrow{font-size:23px;color:var(--green);font-weight:500}
.lead{font-size:13.5px;font-weight:600;color:var(--white);line-height:23px}
.body{font-size:11.5px;line-height:22px;color:var(--text)}
.btn{display:inline-block;border:1.5px solid var(--white);border-radius:20px;padding:0 22px;height:32px;line-height:30px;font-size:11px;color:var(--white);font-weight:500}
/* about */
.about{height:630px;background:var(--bg)}
.about-text{left:0;top:0;width:612px;height:630px;background:var(--bg-panel)}
.about-text .eyebrow{position:absolute;left:63px;top:46px}
.acc{position:absolute;left:63px;width:462px;display:flex;align-items:center;gap:10px;font-size:14px;color:var(--green)}
.acc .line{flex:1;height:1px;background:var(--green)}
.acc .plus{width:18px;height:18px;border:1.5px solid var(--green);border-radius:50%;text-align:center;line-height:14px;font-size:13px}
.about-copy{position:absolute;left:63px;top:140px;width:440px;font-size:11.5px;line-height:16px;color:var(--text)}
.about-copy p{margin-bottom:15px}
/* pricing */
.pricing{height:628px;background:var(--bg)}
.pricing h2{position:absolute;left:0;width:1200px;top:46px;text-align:center;font-size:23px;font-weight:400;color:var(--green)}
.spec-title{font-size:15px;font-weight:500;color:var(--white)}
.spec-price{font-size:15px;color:var(--green);margin-top:10px}
.spec{margin-top:32px}
.spec b{display:block;font-weight:400;font-size:19px;color:var(--green)}
.spec span{font-size:11px;color:var(--text)}
/* forms */
.forms{height:635px;background:var(--bg)}
.form-title{position:absolute;left:0;width:1200px;text-align:center;font-size:20px;font-weight:400;color:var(--white)}
.field{position:absolute;height:32px;background:var(--field);font-size:11.5px;color:var(--muted);padding-left:22px;line-height:32px}
.submit{position:absolute;left:537px;width:126px;height:32px;border:1.5px solid var(--white);border-radius:20px;text-align:center;line-height:29px;font-size:11px;font-weight:600;color:var(--white)}
/* footer */
.footer{height:631px;background:var(--bg-deep)}
.footer .wordmark{left:0;width:1200px;text-align:center;top:70px;font-size:26px}
.contact{top:295px;width:300px;text-align:center;font-size:11.5px;line-height:21px;color:var(--white)}
.contact svg{display:block;margin:0 auto 12px}
.social{display:flex;gap:8px;justify-content:center;margin-bottom:12px}
.social i{width:24px;height:24px;border:1.5px solid var(--white);border-radius:50%}
.social i.on{border-color:var(--green)}
.foot-nav{left:0;width:1200px;top:546px;display:flex;justify-content:center;gap:36px;font-size:12px;color:var(--white)}
.foot-nav .active{color:var(--green)}
.copyright{left:0;width:1200px;top:576px;text-align:center;font-size:10.5px;color:var(--muted)}
</style>
</head>
<body>

<header class="section hero">
  <div class="abs wordmark">Quill Stone Solar</div>
  <nav class="abs nav"><span class="active">Home</span><span>About Us</span><span>Products</span><span>Package Deals</span><span>Contact</span></nav>
  <h1 class="abs hero-title">OFF-GRID LITHIUM SOLAR<br>ENERGY SOLUTIONS</h1>
  <div class="abs feature" style="left:161px">
    <svg width="64" height="64" viewBox="0 0 64 64" fill="none" stroke="#fff" stroke-width="2.5"><circle cx="32" cy="12" r="5"/><path d="M32 2v3M22 12h-3M45 12h-3M25 5l2 2M39 5l-2 2"/><path d="M14 54l6-28h24l6 28z"/><path d="M17 40h30M28 26l-2 28M36 26l2 28"/></svg>
    Solar Panel Bundle
  </div>
  <div class="abs feature" style="left:470px">
    <svg width="64" height="64" viewBox="0 0 64 64" fill="none" stroke="#fff" stroke-width="2.5"><rect x="8" y="12" width="48" height="42" rx="6"/><path d="M22 8h20"/><rect x="15" y="20" width="34" height="14" rx="2"/><circle cx="40" cy="44" r="3"/><circle cx="48" cy="44" r="2"/></svg>
    Smart Inverter Controller
  </div>
  <div class="abs feature" style="left:754px">
    <svg width="64" height="64" viewBox="0 0 64 64" fill="none" stroke="#fff" stroke-width="2.5"><rect x="20" y="10" width="24" height="46" rx="4"/><path d="M27 6h10"/><path d="M34 20l-7 13h9l-7 13" stroke-linejoin="round"/></svg>
    Lithium Battery Packs
  </div>
</header>

<section class="section about">
  <div class="abs about-text">
    <h2 class="eyebrow">About Us</h2>
    <div class="acc" style="top:96px"><span>The Passion Behind The Quill Stone SolarThe Team</span><span class="line"></span><span class="plus">−</span></div>
    <div class="about-copy">
      <p>After 20 plus years of designing, building and installing world leading, award winning and mission critical electrical and electronic solutions around the world. The management team at Quill Stone Solar are now offering 'Turn-Key' energy storage solutions for the Bay of Islands and Northland.</p>
      <p>We are passionate about renewable energy and believe in solutions that protect our environment. As off-grid evangelists in Aotearoa's magical Northland, We feel we have an obligation to sell solutions that promotes this passion.</p>
      <p>The clean environmentally friendly hardware, solutions and services we provide echo this belief. On hardware we have pushed our manufacturers to provide the longest and fullest warranties on products.</p>
    </div>
    <div class="acc" style="top:431px"><span>The Panel and Framing Installers</span><span class="line"></span><span class="plus">+</span></div>
    <div class="acc" style="top:467px"><span>Our Registered Electricians</span><span class="line"></span><span class="plus">+</span></div>
    <div class="acc" style="top:503px"><span>Servicing and Repairs Department</span><span class="line"></span><span class="plus">+</span></div>
  </div>
  <div class="abs photo" role="img" aria-label="Photo of a white two-storey house with solar panels on its dark roof" style="left:612px;width:588px;background:linear-gradient(180deg,#d9dde2 0%,#c4c8cc 40%,#5b6068 65%,#8d9094 100%)"></div>
</section>

<section class="section split" style="background:var(--bg-deep)">
  <div class="abs photo" role="img" aria-label="Aerial photo of a yellow house with a solar panel roof among trees" style="left:0;width:832px;background:linear-gradient(160deg,#6f8a4c 0%,#3f4a6a 40%,#d6b784 70%,#7e8f55 100%)"></div>
  <div class="abs" style="left:878px;top:48px;width:290px">
    <h2 class="eyebrow">How it works</h2>
    <p class="lead" style="margin-top:22px">Lorem Ipsum is simply dummy text of the printing and typesetting industry.</p>
    <p class="body" style="margin-top:16px">Lorem Ipsum has been the industry's standard dummy text ever since the 1500s, when an unknown printer took a galley of type and scrambled it to make a type specimen book.</p>
    <div class="btn" style="margin-top:24px;color:var(--green)">READ MORE</div>
  </div>
</section>

<section class="section split" style="background:var(--bg)">
  <div class="abs" style="left:46px;top:48px;width:310px">
    <h2 class="eyebrow">Mobile</h2>
    <p class="lead" style="margin-top:20px">Lorem Ipsum is simply dummy text of the printing and typesetting industry.</p>
    <p class="body" style="margin-top:16px">Lorem Ipsum has been the industry's standard dummy text ever since the 1500s, when an unknown printer took a galley of type and scrambled it to make a type specimen book.</p>
    <div class="btn" style="margin-top:24px">READ MORE</div>
  </div>
  <div class="abs" role="img" aria-label="Phone showing the monitoring app, grid mode" style="left:506px;top:140px;width:195px;height:356px;border-radius:12px;background:linear-gradient(180deg,#2a2a2a,#1a1d22)"></div>
  <div class="abs" role="img" aria-label="Phone showing the monitoring app, offline mode" style="left:717px;top:140px;width:195px;height:356px;border-radius:12px;background:linear-gradient(180deg,#2a2a2a,#1a1d22)"></div>
  <div class="abs" role="img" aria-label="Phone showing the monitoring app, charging mode" style="left:928px;top:140px;width:195px;height:356px;border-radius:12px;background:linear-gradient(180deg,#2a2a2a,#1a1d22)"></div>
</section>

<section class="section split" style="background:var(--bg-deep)">
  <div class="abs photo" role="img" aria-label="Photo of an installer fitting solar panels on a roof under a blue sky" style="left:0;width:832px;background:linear-gradient(170deg,#8fb6e6 0%,#3a57b0 45%,#1f2f7a 80%,#5c4a3e 100%)"></div>
  <div class="abs" style="left:878px;top:42px;width:290px">
    <h2 class="eyebrow" style="line-height:31px">Home installation<br>location</h2>
    <p class="lead" style="margin-top:20px">Lorem Ipsum is simply dummy text of the printing and typesetting industry.</p>
    <p class="body" style="margin-top:16px">Lorem Ipsum has been the industry's standard dummy text ever since the 1500s, when an unknown printer took a galley of type and scrambled it to make a type specimen book.</p>
    <div class="btn" style="margin-top:24px">READ MORE</div>
  </div>
</section>

<section class="section pricing">
  <h2>Turn Key Solutions and Prices</h2>
  <div class="abs" role="img" aria-label="Two solar panels floating in perspective" style="left:114px;top:177px;width:530px;height:294px;background:linear-gradient(180deg,transparent 0%,#1e2f6e 10%,#2c3f8c 40%,transparent 48%,transparent 52%,#1e2f6e 60%,#2c3f8c 92%,transparent 100%)"></div>
  <div class="abs" style="left:755px;top:120px;width:400px">
    <div class="spec-title">SUMMIT - 40KW COMMERCIAL BUSINESS</div>
    <div class="spec-price">$51,995 inc GST</div>
    <div class="spec"><b>40 kWh</b><span>Qty 4 of the 51V Lithium Battery Systems</span></div>
    <div class="spec"><b>10kW</b><span>Qty 4 of the 51V Lithium Battery Systems</span></div>
    <div class="spec"><b>8.0kW</b><span>Solar Array - 20 x Azure Ray 400W Monocrystalline Panels</span></div>
    <div class="spec"><b>10kVA</b><span>Auto Starting Diesel Generator</span></div>
    <div class="btn" style="margin-top:30px;height:30px;line-height:27px;font-size:10.5px">SHOP NOW</div>
  </div>
</section>

<section class="section forms">
  <h2 class="form-title" style="top:84px">Request Solutions Consultant</h2>
  <div class="field" style="left:141px;top:139px;width:300px">Name</div>
  <div class="field" style="left:449px;top:139px;width:300px">Email</div>
  <div class="field" style="left:758px;top:139px;width:301px">Phone</div>
  <div class="submit" style="top:206px">SUBMIT</div>

  <h2 class="form-title" style="top:330px">Estimator</h2>
  <div class="field" style="left:141px;top:378px;width:300px">First Name</div>
  <div class="field" style="left:449px;top:378px;width:300px">Email</div>
  <div class="field" style="left:758px;top:378px;width:301px">Phone</div>
  <div class="field" style="left:141px;top:421px;width:918px">Contact Time Preference</div>
  <div class="submit" style="top:480px">SUBMIT</div>
</section>

<footer class="section footer">
  <div class="abs wordmark">Quill Stone Solar</div>
  <div class="abs contact" style="left:180px">
    <svg width="26" height="22" viewBox="0 0 26 22" fill="none" stroke="#fff" stroke-width="2"><rect x="1" y="2" width="24" height="18" rx="2"/><path d="M1 4l12 9 12-9"/></svg>
    hello@quillstonesun-example.co.nz<br>0200 555 018
  </div>
  <div class="abs contact" style="left:455px">
    <svg width="26" height="24" viewBox="0 0 26 24" fill="none" stroke="#fff" stroke-width="2" stroke-linejoin="round"><path d="M2 11L13 2l11 9M5 9v13h16V9"/><path d="M10 22v-7h6v7"/></svg>
    Tarrow Bay 0471<br>Northland, New Zealand
  </div>
  <div class="abs contact" style="left:710px;top:290px">
    <div class="social"><i></i><i></i><i class="on"></i></div>
    Follow us
  </div>
  <nav class="abs foot-nav"><span class="active">Home</span><span>About Us</span><span>Products</span><span>Package Deals</span><span>Contact</span></nav>
  <div class="abs copyright">Copyright © Quill Stone Solar. All Rights Reserved</div>
</footer>

</body>
</html>
```